Brindle's Business Card

I need some designs for a new business card including the new logo attached. An old example of our business card is also attached to show all the data that should be included on the new design.
**I added some more examples someone had mocked up**

Contact Information for Business Card

Should include all info on other examples uploaded.

```html
<!DOCTYPE html>
<html lang="en">
<head>
<meta charset="utf-8">
<title>Brindle's Business Card</title>
<link rel="stylesheet" href="https://fonts.googleapis.com/css2?family=Montserrat:wght@500;600&family=Poppins:wght@300;400;600&family=Bebas+Neue&display=swap">
<style>
  :root {
    --brand-blue: #0071bd;
    --brand-red: #ed1c24;
    --paper: #ffffff;
    --backdrop: #2d2d2d;
  }
  * { box-sizing: border-box; margin: 0; padding: 0; }
  html, body { width: 1093px; height: 1200px; overflow: hidden; }
  body { background: var(--backdrop); position: relative; font-family: 'Poppins', sans-serif; }

  .card {
    position: absolute;
    width: 578px;
    height: 357px;
    overflow: hidden;
    box-shadow: 2px 3px 6px rgba(0,0,0,0.6);
  }
  .card--front { left: 265px; top: 226px; background: var(--paper); }
  .card--back { left: 265px; top: 620px; width: 581px; background: var(--brand-blue); }

  /* front */
  .front__band {
    position: absolute; left: 0; top: 189px; width: 300px; height: 168px;
    background: var(--brand-blue);
  }
  .front__mark {
    position: absolute; left: 300px; top: 110px; width: 280px; height: 280px;
    border-radius: 50%; background: var(--brand-blue);
    border: 13px solid var(--brand-red);
  }
  .front__company {
    position: absolute; left: 32px; top: 52px;
    font-family: 'Montserrat', sans-serif; font-weight: 600;
    font-size: 46px; line-height: 1; color: var(--brand-blue); letter-spacing: 0.5px;
  }
  .front__tagline {
    position: absolute; left: 34px; top: 98px;
    font-family: 'Montserrat', sans-serif; font-weight: 500;
    font-size: 12px; color: var(--brand-red); letter-spacing: 0.2px;
  }
  .front__person {
    position: absolute; left: 33px; top: 154px;
    font-weight: 600; font-size: 23px; line-height: 1; color: var(--brand-red);
  }
  .contact { position: absolute; left: 33px; display: flex; align-items: center; gap: 9px;
    color: var(--paper); font-weight: 300; font-size: 17px; line-height: 1; }
  .contact--phone { top: 208px; }
  .contact--email { top: 231px; }
  .contact__icon { width: 18px; height: 18px; flex: none; }
  .front__rule { position: absolute; left: 35px; top: 264px; width: 244px; height: 1px; background: var(--paper); }
  .front__claims { position: absolute; left: 38px; top: 281px; color: var(--paper);
    font-weight: 600; font-size: 16px; line-height: 23.5px; }

  /* back */
  .back__dot { position: absolute; left: 87px; top: 86px; width: 96px; height: 96px;
    border-radius: 50%; background: var(--paper); }
  .back__name { position: absolute; left: 190px; top: 101px;
    font-family: 'Montserrat', sans-serif; font-weight: 600;
    font-size: 57px; line-height: 1; color: var(--paper); }
  .back__tagline { position: absolute; left: 192px; top: 158px;
    font-family: 'Montserrat', sans-serif; font-weight: 500; font-size: 14.6px;
    line-height: 1; color: var(--brand-red); }
  .back__area { position: absolute; left: 0; right: 0; top: 206px; text-align: center;
    color: var(--paper); font-size: 17px; font-weight: 400; }
  .back__cta { position: absolute; left: 0; right: 0; top: 259px; height: 37px;
    background: var(--brand-red); color: var(--paper); text-align: center;
    font-family: 'Bebas Neue', sans-serif; font-size: 25px; line-height: 39px; letter-spacing: 0.2px; }
</style>
</head>
<body>
  <section class="card card--front">
    <div class="front__band"></div>
    <div class="front__mark"></div>
    <h1 class="front__company">BRINDLE'S</h1>
    <p class="front__tagline">AIR CONDITIONING &amp; HEATING SERVICE</p>
    <h2 class="front__person">DALE BRINDLE</h2>
    <p class="contact contact--phone">
      <svg class="contact__icon" viewBox="0 0 24 24" aria-hidden="true"><path fill="#ed1c24" d="M6.6 10.8a15.1 15.1 0 0 0 6.6 6.6l2.2-2.2a1 1 0 0 1 1-.25 11.4 11.4 0 0 0 3.6.57 1 1 0 0 1 1 1V20a1 1 0 0 1-1 1A17 17 0 0 1 3 4a1 1 0 0 1 1-1h3.5a1 1 0 0 1 1 1c0 1.25.2 2.45.57 3.6a1 1 0 0 1-.25 1z"/></svg>
      555.014.2290
    </p>
    <p class="contact contact--email">
      <svg class="contact__icon" viewBox="0 0 24 24" aria-hidden="true"><rect x="2" y="5" width="20" height="14" fill="#ed1c24"/><path d="M2 5l10 8 10-8" fill="none" stroke="#0071bd" stroke-width="1.6"/></svg>
      hvacbrindle@mail.com
    </p>
    <div class="front__rule"></div>
    <p class="front__claims">LICENSED &amp; INSURED<br>FAMILY OWNED &amp; OPERATED</p>
  </section>

  <section class="card card--back">
    <span class="back__dot"></span>
    <h2 class="back__name">BRINDLE'S</h2>
    <p class="back__tagline">AIR CONDITIONING &amp; HEATING SERVICE</p>
    <p class="back__area">Serves Cedar Bend, IA &amp; Surrounding Areas</p>
    <p class="back__cta">CALL TODAY FOR ALL YOUR HVAC, REFRIGERATION &amp; PLUMBING NEEDS</p>
  </section>
</body>
</html>
```